A modern, fresh introduction to Buddhism

I need a book cover for an A6 sized book to be used both for ebook and hard copy. The author is a young, modern Buddhist teacher of high standing who has written this short intro to Buddhism in an informal Q & As format using modern, accessible language to convey profound and meaningful ideas to the general public. The author is Tibetan, but teaches worldwide and is very personable and dynamic. The cover should portray this and have a fresh yet authentic feel to it (nothing new-agey!). Please see the author's websites www.norvalemtasheteacher.org and www.pwrt.org for reference, but do not feel that the design must align completely with the website designs.

Target Market(s)

General public both in Europe and America and in Asia ranging from teenagers to the elderly. A really broad audience.

Industry/Entity Type

Teacher

Requirements
Must have
• Please include the following text that on the front cover:

A Window onto Stillness

By Drawa Tsomen Lhundrup

Please include the following on the back cover:

Yunor Trenpa Publications (with attached logo above it)
Nice to have
• A simplistic, artistic, and modern look without any traditional religious images.
Should not have
• No buddha images or religious images. I would prefer a more simplistic, modern and artistic look.

```html
<!DOCTYPE html>
<html lang="en">
<head>
<meta charset="utf-8">
<title>A Window onto Stillness – Book Cover</title>
<link rel="stylesheet" href="https://fonts.googleapis.com/css2?family=Arimo:wght@400;700&display=swap">
<style>
  :root {
    --page-bg: #ffffff;
    --cover-bg: #f1f1f1;
    --ink-blue: #2e3192;
    --ink-red: #ed1c24;
    --cover-edge: #3a3a3a;
    --shadow: rgba(0, 0, 0, 0.45);
  }
  * { margin: 0; padding: 0; box-sizing: border-box; }
  html, body {
    width: 1200px;
    height: 848px;
    overflow: hidden;
    background: var(--page-bg);
    font-family: "Arimo", Arial, sans-serif;
  }
  .spread {
    position: relative;
    width: 1200px;
    height: 848px;
  }
  .cover {
    position: absolute;
    background: var(--cover-bg);
    box-shadow: 8px 8px 7px var(--shadow);
    overflow: hidden;
  }
  .cover--front {
    left: 130px; top: 48px;
    width: 417px; height: 631px;
    border: 1px solid var(--cover-edge);
  }
  .cover--back {
    left: 658px; top: 50px;
    width: 412px; height: 634px;
  }
  .pattern-field {
    position: absolute;
    display: block;
    z-index: 0;
  }
  .cover--front .pattern-field { left: 0; top: 283px; }
  .cover--back .pattern-field { right: 0; top: 285px; }

  .title {
    position: absolute;
    left: 40px; top: 86px;
    font-weight: 700;
    font-size: 19px;
    line-height: 24px;
    letter-spacing: 0.12em;
    text-transform: uppercase;
  }
  .title__line--lead { color: var(--ink-blue); letter-spacing: 0.16em; }
  .title__line--main { color: var(--ink-red); letter-spacing: 0.02em; }
  .author {
    position: absolute;
    z-index: 1;
    left: 177px; top: 596px;
    font-weight: 700;
    font-size: 13px;
    white-space: nowrap;
    color: var(--ink-blue);
  }
  .publisher {
    position: absolute;
    left: 0; right: 0; top: 80px;
    display: flex;
    flex-direction: column;
    align-items: center;
    gap: 18px;
  }
  .publisher__mark {
    width: 76px; height: 76px;
    border-radius: 50%;
    border: 1.5px solid var(--ink-blue);
  }
  .publisher__name {
    font-weight: 700;
    font-size: 11px;
    color: var(--ink-blue);
  }
</style>
</head>
<body>
<main class="spread">
  <section class="cover cover--front">
    <h1 class="title">
      <span class="title__line title__line--lead">A Window onto</span><br>
      <span class="title__line title__line--main">Stillness</span>
    </h1>
    <svg class="pattern-field" width="286" height="348" viewBox="0 0 286 348" role="img" aria-label="Interlocking blue rings pattern with red petal crossings">
      <defs>
        <linearGradient id="ringToneFront" x1="0" y1="0" x2="1" y2="1">
          <stop offset="0" stop-color="#4a4ea6"/>
          <stop offset="0.5" stop-color="#7a4c98"/>
          <stop offset="1" stop-color="#3d41a0"/>
        </linearGradient>
      </defs>
      <polygon points="0,0 162,0 286,126 286,212 204,300 166,304 166,348 0,348" fill="url(#ringToneFront)"/>
    </svg>
    <p class="author">By Drawa Tsomen Lhundrup</p>
  </section>

  <section class="cover cover--back">
    <div class="publisher">
      <span class="publisher__mark" aria-hidden="true"></span>
      <p class="publisher__name">Yunor Trenpa Publications</p>
    </div>
    <svg class="pattern-field" width="283" height="349" viewBox="0 0 283 349" role="img" aria-label="Interlocking blue rings pattern with red petal crossings">
      <defs>
        <linearGradient id="ringToneBack" x1="1" y1="0" x2="0" y2="1">
          <stop offset="0" stop-color="#4a4ea6"/>
          <stop offset="0.5" stop-color="#7a4c98"/>
          <stop offset="1" stop-color="#3d41a0"/>
        </linearGradient>
      </defs>
      <polygon points="283,0 122,0 0,127 0,215 117,349 283,349" fill="url(#ringToneBack)"/>
    </svg>
  </section>
</main>
</body>
</html>
```